Landing Page for Martial Arts School

We'd like our page to look very much like http://www.tallpinestudio.com/. I've attached our text and you can see how I've tried to make it similar to their site in placement.
We'd like to do a darker green instead of their blue shading, obviously our logo (the dragon image) instead of theirs, our student photo or a better image you may choose, and instead of a solid block of text under "Welcome . . ." we'd like the USA Badge to the right of the text. At the bottom of the page we'd like a big button with our phone number. I know this is a lot to take in, but we're so looking forward to seeing your designs!

These designs are looking good! I'm sending each of you a few suggested tweaks for now! Best of luck!

As we enter the final few days of competition, I'd like to give a final word of thanks to all of our designers. We have moved out of good and into excellent, and we thank you all. We've also updated the student image we'd like you to use. All of the remaining designers will need to update their photos with the new one, please. Also, if you've one of the final designs, I'll be sending you a final set of notes and then we will be selecting someone. We may push back the final selection until Monday, depending.

Reason: We're going to discuss the finalized versions of your designs on Monday and make our final selection. If for some reason, none of the designers have made our suggested tweaks, then we still have another day.

```html
<!DOCTYPE html>
<html lang="en">
<head>
<meta charset="utf-8">
<title>Summit Ridge TaeKwonDo</title>
<link href="https://fonts.googleapis.com/css2?family=Open+Sans:wght@400;600&family=Signika:wght@500;600&display=swap" rel="stylesheet">
<style>
:root{
  --green:#5f9a1e;
  --green-light:#9ccb2c;
  --green-mid:#72a824;
  --green-dark:#4a7209;
  --ink:#2a2a2a;
  --nav:#333;
  --gray-bg:#ececec;
  --white:#fff;
  --brand-red:#d0202a;
}
*{margin:0;padding:0;box-sizing:border-box}
html,body{width:1143px;height:1200px;overflow:hidden;background:var(--white)}
body{font-family:"Open Sans",Arial,sans-serif;color:var(--ink);position:relative}
.header{position:absolute;left:0;top:0;width:1143px;height:128px;background:linear-gradient(#fafafa,#fff 60%,#f4f4f4);border-bottom:1px solid #e2e2e2}
.brand{position:absolute;left:186px;top:14px;width:102px;height:102px;display:flex;align-items:center;justify-content:center;text-align:center}
.brand svg{position:absolute;left:0;top:0}
.brand-name{position:relative;font-family:"Signika",sans-serif;font-weight:600;font-size:14px;line-height:16px;color:var(--brand-red)}
.nav{position:absolute;left:433px;top:62px;display:flex;align-items:center;font-family:"Signika",sans-serif;font-weight:600;font-size:16px;color:var(--nav);letter-spacing:.3px}
.nav span{padding:0 12px;border-left:1px solid #ccc;line-height:12px}
.nav span:first-child{border-left:0;padding-left:0}
.cta{position:absolute;left:839px;top:24px;width:134px;height:80px;background:linear-gradient(var(--green-light),var(--green));color:var(--white);font-family:"Signika",sans-serif;font-weight:600;font-size:11.5px;line-height:16px;padding:17px 0 0 19px;letter-spacing:.2px}
.hero{position:absolute;left:0;top:129px;width:1143px;height:420px;background:linear-gradient(100deg,#e9ddd0 0%,#d9b9a0 25%,#5a9a3a 50%,#c4473e 62%,#3a8ac0 75%,#6aa654 88%,#cfc3b6 100%)}
.welcome{position:absolute;left:0;top:549px;width:1143px;height:260px;background:var(--gray-bg)}
.welcome h1{position:absolute;left:169px;top:24px;font-family:"Signika",sans-serif;font-weight:600;font-size:18px;color:var(--green);letter-spacing:.4px}
.welcome p{position:absolute;left:169px;width:806px;font-size:11.3px;line-height:19px}
.classes{position:absolute;left:0;top:809px;width:1143px;height:231px}
.class-row{position:absolute;left:172px;display:flex}
.class-row h2{width:261px;font-family:"Signika",sans-serif;font-weight:600;font-size:20px;color:var(--green);letter-spacing:.3px}
.class-row p{width:510px;font-size:11.3px;line-height:18.5px;padding-top:3px}
.contact-band{position:absolute;left:0;top:1040px;width:1143px;height:113px;background:linear-gradient(var(--green-light),var(--green-mid));text-align:center;color:var(--white);font-family:"Signika",sans-serif;font-weight:600;font-size:20px;line-height:34px;padding-top:22px}
.footer{position:absolute;left:0;top:1153px;width:1143px;height:47px;background:var(--green-dark);color:var(--white);text-align:center;font-size:11.8px;line-height:47px}
</style>
</head>
<body>
<header class="header">
  <div class="brand">
    <svg width="102" height="102" viewBox="0 0 102 102"><circle cx="51" cy="51" r="49" fill="none" stroke="#d0202a" stroke-width="2"/></svg>
    <span class="brand-name">Summit<br>Ridge</span>
  </div>
  <nav class="nav"><span>HOME</span><span>ABOUT US</span><span>OUR CLASSES</span><span>CONTACT US</span></nav>
  <div class="cta">CALL TODAY FOR A<br>FREE LESSON<br>555 214-7730</div>
</header>
<div class="hero" role="img" aria-label="Photo of a row of young students smiling in a bright classroom"></div>
<section class="welcome">
  <h1>WELCOME TO SUMMIT RIDGE TAEKWONDO!</h1>
  <p style="top:61px">Are you interested in Summit Ridge TaeKwonDo classes, lessons, sparring, training, or one-on-one private tutoring in the martial arts? We are a full time martial arts academy based in Ashford, TN. We offer a range of TaeKwonDo, or Korean Karate, classes for all skill levels, but we specialize in TaeKwonDo for kids and teens!</p>
  <p style="top:136px">TaeKwonDo training is in a safe, friendly school under the car of an instructor with 20 years of experience in martial arts. Our Instructor, Dan Holloway, was voted 2014’s Children’s Instructor of the Year by the National Martial Arts Honor Guild! Learn with the best!</p>
  <p style="top:193px">We are located at 48 W. Linden Street right in Downtown, Ashford, TN. One block East of Hartley’s Grill, across the street from Ashford Arts Center, Two Doors Down from Bluebird Music Hall, and directly between Marlow’s on Linden and Stillwater Yoga.</p>
</section>
<section class="classes">
  <div class="class-row" style="top:35px"><h2>Beginners (ages 3-7)</h2><p>It is a fun, energetic introduction to the art. Students begin to learn forms. This class accepts young students.</p></div>
  <div class="class-row" style="top:88px"><h2>Intermediate (ages 6-15)</h2><p>Children learn martial arts, respect, and self-defense in a safe environment. This class is based on experience level and accepts students with some experience in the art.</p></div>
  <div class="class-row" style="top:143px"><h2>Advanced (ages 8-14)</h2><p>For students who have some experience past the basic level. We cover more advanced topics, higher-kicks and more sparring. We prep our students for the challenges of confrontation, bullying, and self-defense.</p></div>
</section>
<section class="contact-band">We’d Love to Hear From You!<br>Call 555 214-7730</section>
<footer class="footer">48 W Linden Street Ashford, TN 37900</footer>
</body>
</html>
```